Fiscal Sponsorship Program Flyer

We are seeking a designer to create a 1-2 flyer that explains our fiscal sponsorship program. This flyer will be used to recruit new projects that might be interested in utilizing our fiscal sponsorship services. The pertinent information about our program can be found in the attached PDF. For users who cannot access the PDF, please try this link: https://files.brivanto.net/slides/d/7QtR2wXkLmZp9HvCs4YdNe8JfGaUoBi3Tx5Wl0KyRc2s/view?mode=shared

Target Market(s)

New charitable projects that do not yet have their own 501(c)(3) status, and are seeking a fiscal sponsor.

Industry/Entity Type

Nonprofit/Charity

Requirements
Must have
• The flyer must include the language and detail included on the attached PDF. The desire is to reformat this to be more appealing and easy to read.

```html
<!DOCTYPE html>
<html lang="en">
<head>
<meta charset="utf-8">
<title>Meridian Foundation – Fiscal Sponsorship Program</title>
<link rel="stylesheet" href="https://fonts.googleapis.com/css2?family=Merriweather:wght@400;700;900&display=swap">
<style>
:root{
  --backdrop:#e4ebef;
  --teal:#5f98a3;
  --teal-deep:#4d8591;
  --navy:#0b1838;
  --red:#f20000;
  --white:#ffffff;
  --paper:#ffffff;
  --mist:#dfe7ed;
  --ink-soft:#5b8a99;
  --ink-pale:#9cc0c8;
}
*{margin:0;padding:0;box-sizing:border-box}
html,body{width:849px;height:1200px;overflow:hidden}
body{background:var(--backdrop);font-family:"Merriweather",Georgia,serif;position:relative;color:var(--navy)}
.spread{position:absolute;left:124px;width:600px;height:424px;display:flex;box-shadow:0 3px 8px rgba(20,40,60,.35)}
.spread--outer{top:195px}
.spread--inner{top:682px}
.page{position:relative;width:300px;height:424px;overflow:hidden}
.abs{position:absolute}
.vline{position:absolute;width:1px;background:var(--navy)}
.vline--red{background:var(--red)}
.vline--soft{background:var(--ink-soft)}

/* fee page */
.page--fees{background:var(--teal)}
.section-title{font-weight:700;font-size:10px;line-height:12px}
.section-title .accent{color:var(--red)}
.fee-tag{position:absolute;left:102px;width:136px;height:15px;background:var(--red);color:var(--white);font-size:6.6px;line-height:15px;padding-left:5px}
.fee-list{position:absolute;left:102px;font-size:4.4px;line-height:8.1px;color:var(--navy)}
.fee-list--wide{line-height:9px}
.team-heading{position:absolute;left:97px;top:295px;font-size:4.3px;font-weight:700;color:var(--navy)}
.team{position:absolute;left:34px;top:310px;display:flex;gap:5.6px}
.member{width:42px}
.member__photo{width:42px;height:56px;background:linear-gradient(160deg,#d9d9d9,#7a7a7a 70%,#3c3c3c)}
.member__name{font-size:3.4px;font-weight:700;margin-top:3px;color:var(--navy);white-space:nowrap}
.member__role{font-size:3px;color:#3f7482}
.footer-line{position:absolute;left:0;width:300px;text-align:center;font-size:4.3px;font-weight:700;top:388px}
.page--fees .footer-line{color:var(--white)}
.brand-mark{position:absolute;display:flex;align-items:center;gap:2px;font-weight:700}
.brand-mark__dot{border-radius:50%;border:1px solid currentColor}

/* cover */
.page--cover{background:linear-gradient(180deg,#5f97a2 0%,#78aab2 35%,#5f8aa5 60%,#2c4f72 100%)}
.cover-photo{position:absolute;left:0;top:160px;width:300px;height:264px;background:linear-gradient(170deg,rgba(220,150,120,.0) 0%,rgba(232,160,130,.55) 30%,rgba(200,215,230,.7) 45%,rgba(70,110,150,.75) 75%,rgba(30,55,85,.85) 100%)}
.cover-title{position:absolute;left:42px;top:30px;color:var(--white);font-weight:900;font-size:33px;line-height:33px}
.cover-label{position:absolute;left:42px;background:var(--red);color:var(--white);font-weight:900;font-size:14.5px;line-height:17px;padding:0 4px}
.cover-nav{position:absolute;left:0;width:300px;text-align:center;font-size:4.3px;color:var(--ink-pale);line-height:9px}
.cover-nav span{margin:0 6px}
.page--cover .footer-line{color:var(--white)}

/* inner left */
.page--about{background:var(--paper)}
.about-photo{position:absolute;left:0;top:0;width:300px;height:81px;background:linear-gradient(180deg,#6ea2ab 0%,#7fb0b6 45%,#d89a83 58%,#5f8aa0 72%,#2f5577 100%)}
.about-title{position:absolute;left:32px;font-weight:700;font-size:10px;line-height:12px;color:var(--navy)}
.about-title .accent{color:var(--red)}
.about-title .blue{color:#2d5b7a}
.about-text{position:absolute;left:109px;width:166px;font-size:4.3px;line-height:8px;color:var(--ink-soft);text-align:justify}
.about-text p+p{margin-top:4px}
.about-text b{color:var(--navy)}
.red-rule{position:absolute;left:34px;width:242px;height:2.5px;background:var(--red)}
.faint-mark{position:absolute;left:14px;top:150px;width:140px;height:140px;border-radius:50%;border:4px solid rgba(190,210,220,.25)}
.page--about .footer-line{color:var(--navy)}

/* inner right */
.page--values{background:var(--mist)}
.values-text{position:absolute;left:125px;width:146px;font-size:4.3px;line-height:7px;color:var(--ink-soft);text-align:justify}
.values-text p{margin-bottom:5.5px}
.values-text b{color:var(--navy)}
.mission-box{position:absolute;left:30px;top:170px;width:243px;height:77px;background:var(--navy);color:var(--white);font-size:4.3px;line-height:8px;padding:9px 13px;text-align:justify}
.commit-list{position:absolute;left:123px;top:262px;width:150px;list-style:none;font-size:4.3px;line-height:7px;color:var(--navy)}
.commit-list li{position:relative;padding-left:10px;margin-bottom:4.6px;text-align:justify}
.commit-list li::before{content:"";position:absolute;left:0;top:1.5px;width:4px;height:4px;background:#2d5b7a}
.page--values .footer-line{color:var(--ink-soft)}
</style>
</head>
<body>

<section class="spread spread--outer">
  <article class="page page--fees">
    <h2 class="section-title abs" style="left:30px;top:51px"><span class="accent">Fee</span><br>Structure</h2>

    <div class="vline" style="left:89px;top:36px;height:79px"></div>
    <div class="fee-tag" style="top:37px">BASIC FEE - 4% (Limited)</div>
    <ul class="fee-list" style="top:55px;list-style:none">
      <li>- Project Fund Set-Up</li>
      <li>- Administration and Management - Financial Management</li>
      <li>- Grant Proposal Review</li>
      <li>- Grant Contract Review</li>
      <li>- Project Reporting</li>
      <li>- Insurance</li>
      <li>- Annual Audit and Form 990</li>
    </ul>

    <div class="vline" style="left:89px;top:130px;height:60px"></div>
    <div class="fee-tag" style="top:132px">STANDARD FEE - 6% (Comprehensive)</div>
    <ul class="fee-list fee-list--wide" style="top:152px;list-style:none">
      <li>Basic Services +</li>
      <li>- Customized Financial Reporting - Monthly Financial Statements</li>
      <li>- Subgranting/regranting to U.S.- based organizations</li>
      <li>- Management of Vendor and Independent Contractors (1099s)</li>
    </ul>

    <div class="vline" style="left:89px;top:205px;height:71px"></div>
    <div class="fee-tag" style="top:207px">PREMIUM FEE - 10% + (Custom)</div>
    <ul class="fee-list" style="top:226px;list-style:none">
      <li>Standard Services + custom services tailored to individual project needs.</li>
      <li>Customization Options:</li>
      <li>- Subgranting/regranting to international organizations</li>
      <li>- Lobbying Filings</li>
      <li>- Project Audit</li>
      <li>- Grant Writing Assistance - One-on-One Coaching</li>
    </ul>

    <div class="brand-mark" style="left:244px;top:280px;color:var(--ink-pale);font-size:4px">
      <span class="brand-mark__dot" style="width:8px;height:8px"></span>Meridian
    </div>

    <h3 class="team-heading">OUR TEAM : BOARD OF DIRECTORS AND STAFF</h3>
    <div class="team">
      <figure class="member"><div class="member__photo" role="img" aria-label="Portrait of board member Owen Ashcroft"></div><figcaption><div class="member__name">OWEN ASHCROFT</div><div class="member__role">board member</div></figcaption></figure>
      <figure class="member"><div class="member__photo" role="img" aria-label="Portrait of board member Miles Carver"></div><figcaption><div class="member__name">MILES CARVER</div><div class="member__role">board member</div></figcaption></figure>
      <figure class="member"><div class="member__photo" role="img" aria-label="Portrait of foundation manager Nina Lorenzo"></div><figcaption><div class="member__name">NINA LORENZO</div><div class="member__role">foundation manager</div></figcaption></figure>
      <figure class="member"><div class="member__photo" role="img" aria-label="Portrait of board member Tamar Elin"></div><figcaption><div class="member__name">TAMAR ELIN</div><div class="member__role">board member</div></figcaption></figure>
      <figure class="member"><div class="member__photo" role="img" aria-label="Portrait of board member Victor Hale"></div><figcaption><div class="member__name">VICTOR HALE</div><div class="member__role">board members</div></figcaption></figure>
    </div>

    <p class="footer-line">email: info@meridianfoundation.org</p>
  </article>

  <article class="page page--cover">
    <div class="cover-photo" role="img" aria-label="Snow-covered mountain peak lit by warm sunrise light"></div>
    <h1 class="cover-title">Meridian<br>Foundation</h1>
    <div class="cover-label" style="top:108px">Fiscal Sponsorship</div>
    <div class="cover-label" style="top:125px">Program</div>
    <div class="vline" style="left:46px;top:172px;height:113px"></div>
    <div class="brand-mark" style="left:232px;top:194px;color:var(--white);font-size:5px">
      <span class="brand-mark__dot" style="width:10px;height:10px"></span>Meridian
    </div>
    <nav class="cover-nav" style="top:352px">
      <div><span>Mission &amp; Vision</span>|<span>What is Fiscal Sponsorship?</span>|<span>Fiscal Sponsorship Program Philosophy</span></div>
      <div><span>Organizational Values</span>|<span>Meridian Foundation - Program Commitments</span>|<span>Fee Structure</span></div>
    </nav>
    <p class="footer-line">www.meridianfoundation.org</p>
  </article>
</section>

<section class="spread spread--inner">
  <article class="page page--about">
    <div class="about-photo" role="img" aria-label="Mountain peak at sunrise against a teal sky"></div>
    <div class="faint-mark"></div>

    <h2 class="about-title" style="top:123px"><span class="accent">Mission</span><br>&amp; Vision</h2>
    <div class="vline vline--soft" style="left:101px;top:107px;height:53px"></div>
    <div class="about-text" style="top:110px">
      <p>The <b>Meridian Foundation</b>, founded in 2010, exists to support social impact campaigns and organizations through educational, public engagement, and awareness efforts.</p>
      <p>Its vision is to strengthen the capacity of the social impact sector and its leaders by providing top-tier fiscal sponsorship services.</p>
    </div>

    <div class="red-rule" style="top:178px"></div>

    <h2 class="about-title" style="top:211px"><span class="blue">What is</span><br>Fiscal<br>Sponsorship</h2>
    <div class="vline vline--soft" style="left:101px;top:201px;height:61px"></div>
    <div class="about-text" style="top:203px">
      <p>What is fiscal sponsorship?</p>
      <p><b>Fiscal sponsorship</b> refers to the practice of non-profit organizations offering their legal and tax-exempt status to charitable projects or groups engaged in activities related to the sponsoring organization's mission. Fiscal sponsors provide oversight, financial management, and other administrative services to build the capacity of charitable projects.</p>
    </div>

    <div class="red-rule" style="top:278px"></div>

    <h2 class="about-title" style="top:311px"><span class="blue">Fiscal<br>Sponsorship</span><br><span class="accent">Program<br>Philosophy</span></h2>
    <div class="vline vline--soft" style="left:101px;top:301px;height:67px"></div>
    <div class="about-text" style="top:304px">
      <p>We believe we can accelerate the pace and scale of social change by providing strategic back office support to emerging projects, leaders and ideas.</p>
      <p>By providing light touch administrative and capacity building services, our fiscal sponsorship program takes the administrative burden off the shoulders of leaders and their projects to allow them to focus on what they do best - achieving impact and changing the world.</p>
    </div>

    <p class="footer-line">www.meridianfoundation.org</p>
  </article>

  <article class="page page--values">
    <h2 class="section-title abs" style="left:28px;top:42px">Organizational<br><span class="accent">Values</span></h2>
    <div class="vline vline--red" style="left:114px;top:31px;height:124px"></div>
    <div class="values-text" style="top:37px">
      <p><b>Trust :</b> We believe that all successful partnerships begin with a foundation of trust.</p>
      <p><b>Relationships :</b> Our partners are central to our work. We honor our relationships through respect, communication and transparency.</p>
      <p><b>Embrace Complexity and Risk:</b> We understand that bold solutions to intractable social issues often require both complexity and risk.</p>
      <p><b>Innovation :</b> We embrace continuous improvement, bold creativity and change.</p>
      <p><b>Diversity :</b> We believe that all voices matter and that effective solutions are created when decision-making is inclusive across social, cultural and economic backgrounds.</p>
    </div>

    <div class="mission-box"><b>Uniting and coordinating</b> the efforts of individuals in order to raise public awareness, promote activism and influence public and individual behavior with respect to charitable programs as defined by section 501(c)(3) including but not limited to the following areas: relief of the poor, the distressed, and the underprivileged; advancement of science and education, lessening the burdens of government; lessening neighborhood tensions, eliminating prejudice and discrimination; defending human and civil rights secured by law, combating community deterioration; and combating juvenile delinquency.</div>

    <h2 class="section-title abs" style="left:28px;top:271px"><span class="accent">Meridian<br>Foundation</span><br>- Program<br>Commitments</h2>
    <div class="vline vline--red" style="left:114px;top:262px;height:112px"></div>
    <ul class="commit-list">
      <li>Fast, simple and efficient fiscal sponsorship program.</li>
      <li>Free and fast approval process - our application can be completed in 30 minutes or less. There is no fee to apply, and most projects can expect to receive a response on their application within 2 weeks.</li>
      <li>No fees and no minimums; projects of any size are welcome to apply.</li>
      <li>Easy onboarding process.</li>
      <li>Dedicated customer service and customization of services, tailored to the individual sponsored project's needs.</li>
      <li>Complex, hybrid structures, partnerships and coalitions are strongly encouraged to apply.</li>
    </ul>
    <div class="brand-mark" style="left:80px;top:354px;color:#2d5b7a;font-size:4px">
      <span class="brand-mark__dot" style="width:9px;height:9px"></span>Meridian
    </div>

    <p class="footer-line">email: info@meridianfoundation.org</p>
  </article>
</section>

</body>
</html>
```